I own a self service Laundromat. From time to time our machines break or take the customers money. I would like to design a post card that I can send the customer that had trouble with one of the machines along with the return of their money. Maybe on one side of the card say OOPS! with a picture of a clothes washer or clothes dryer. On the other side some text that says we are sorry for the trouble at your last visit. Please see attached return of money and we would love to have you back and satisfied. Thank you again for visiting The Suds Corner. I currently don't have a logo so be as creative as you like.

```html
<!DOCTYPE html>
<html lang="en">
<head>
<meta charset="utf-8">
<title>The Suds Corner – Apology Postcard</title>
<link rel="stylesheet" href="https://fonts.googleapis.com/css2?family=Oswald:wght@700&family=Lato:wght@400;700;900&display=swap">
<style>
  :root {
    --backdrop: #d9d9db;
    --card: #ffffff;
    --brand-blue: #1f4fa3;
    --deep-blue: #163a80;
    --sky-blue: #39a6e0;
    --ink: #1b1b1b;
    --charcoal: #2b2d31;
    --stamp: #eadcdc;
    --photo-warm-a: #e8ddd0;
    --photo-warm-b: #b9a48e;
    --photo-shirt-a: #c9a57c;
    --photo-shirt-b: #7d8a98;
  }
  * { box-sizing: border-box; margin: 0; padding: 0; }
  html, body { width: 900px; height: 1200px; overflow: hidden; }
  body {
    background: var(--backdrop);
    font-family: "Lato", Arial, sans-serif;
    position: relative;
  }
  .postcard {
    position: absolute;
    left: 50px;
    width: 800px;
    height: 550px;
    background: var(--card);
    overflow: hidden;
    box-shadow: 0 6px 18px rgba(0,0,0,.25);
  }
  .postcard--front { top: 40px; }
  .postcard--back { top: 630px; }
  .shapes { position: absolute; inset: 0; width: 800px; height: 550px; }

  /* front */
  .headline {
    position: absolute; left: 28px; top: 14px;
    font-family: "Oswald", "Arial Narrow", sans-serif;
    font-size: 74px; line-height: 1; color: var(--brand-blue);
    letter-spacing: 1px;
  }
  .photo-customer {
    position: absolute; left: 0; top: 104px; width: 580px; height: 320px;
    background: linear-gradient(120deg, var(--photo-warm-a) 0%, #d7c6b2 45%, var(--photo-warm-b) 100%);
  }
  .about {
    position: absolute; left: 592px; top: 22px; width: 186px;
    color: #fff; text-align: right;
  }
  .about__title { font-weight: 900; font-size: 20px; letter-spacing: 1px; margin-bottom: 10px; }
  .about__text { font-size: 10.5px; line-height: 1.45; text-align: justify; text-align-last: right; }
  .brand-name {
    position: absolute; right: 28px; bottom: 34px; width: 200px;
    color: #fff; font-weight: 900; font-size: 38px; line-height: 1.02; text-align: right;
  }
  .contact { position: absolute; left: 30px; bottom: 26px; }
  .contact__label { font-weight: 900; font-size: 20px; color: var(--brand-blue); }
  .contact__phone { font-weight: 700; font-size: 22px; color: var(--ink); margin-top: 2px; }
  .contact__web { font-size: 17px; color: var(--ink); margin-top: 4px; }

  /* back */
  .apology {
    position: absolute; left: 22px; top: 20px; width: 370px;
    font-weight: 700; font-size: 20px; line-height: 1.3; color: var(--ink);
  }
  .photo-rack {
    position: absolute; left: 0; top: 150px; width: 400px; height: 290px;
    background: linear-gradient(180deg, var(--photo-shirt-a) 0%, #d9cfc2 40%, var(--photo-shirt-b) 100%);
  }
  .contact--dark { left: 24px; bottom: 24px; }
  .contact--dark .contact__label { color: var(--sky-blue); font-size: 17px; }
  .contact--dark .contact__phone,
  .contact--dark .contact__web { color: #fff; }
  .contact--dark .contact__phone { font-size: 19px; }
  .contact--dark .contact__web { font-size: 15px; }
  .stamp-box {
    position: absolute; right: 26px; top: 24px; width: 82px; height: 96px;
    background: var(--stamp);
  }
</style>
</head>
<body>

<section class="postcard postcard--front">
  <div class="photo-customer" role="img" aria-label="Photo of a smiling woman holding a basket of colourful laundry in a bright home"></div>
  <svg class="shapes" viewBox="0 0 800 550" aria-hidden="true">
    <path d="M0,420 C170,388 360,410 580,330 L580,550 L0,550 Z" fill="var(--card)"/>
    <path d="M0,412 C170,380 360,402 580,322" fill="none" stroke="var(--sky-blue)" stroke-width="6"/>
    <path d="M0,404 C170,372 360,394 580,314" fill="none" stroke="var(--deep-blue)" stroke-width="5"/>
    <path d="M484,0 C560,140 560,330 470,550 L800,550 L800,0 Z" fill="var(--sky-blue)"/>
    <path d="M500,0 C575,140 575,330 488,550 L800,550 L800,0 Z" fill="var(--card)"/>
    <path d="M510,0 C585,140 585,330 498,550 L800,550 L800,0 Z" fill="var(--brand-blue)"/>
  </svg>
  <h1 class="headline">OOPS!</h1>
  <div class="about">
    <h2 class="about__title">ABOUT US</h2>
    <p class="about__text">The Suds Corner is a friendly self service laundromat built for busy people. We keep our washers and dryers clean, fast and ready every day of the week. Bring a single load or a whole family pile and enjoy bright folding tables, free wifi and a calm place to wait. Our team checks every machine often, and when something goes wrong we make it right quickly. Come back soon and let us take care of your clothes.</p>
  </div>
  <div class="brand-name">SUDS CORNER</div>
  <div class="contact">
    <div class="contact__label">CALL US TODAY</div>
    <div class="contact__phone">0198 765 432</div>
    <div class="contact__web">www.sudscorner-laundry.test</div>
  </div>
</section>

<section class="postcard postcard--back">
  <p class="apology">we are sorry for the trouble at your last visit. Please see attached return of money and we would love to have you back and satisfied. Thank you again for visiting The Suds Corner.</p>
  <div class="photo-rack" role="img" aria-label="Photo of freshly cleaned shirts hanging on a rail"></div>
  <svg class="shapes" viewBox="0 0 800 550" aria-hidden="true">
    <path d="M0,395 C140,420 290,410 400,360 L400,550 L0,550 Z" fill="var(--deep-blue)"/>
    <path d="M0,410 C140,432 290,424 400,376 L400,550 L0,550 Z" fill="var(--sky-blue)"/>
    <path d="M0,420 C140,442 290,436 400,390 L400,550 L0,550 Z" fill="var(--charcoal)"/>
  </svg>
  <div class="contact contact--dark">
    <div class="contact__label">CALL US TODAY</div>
    <div class="contact__phone">0198 765 432</div>
    <div class="contact__web">www.sudscorner-laundry.test</div>
  </div>
  <div class="stamp-box"></div>
</section>

</body>
</html>
```